Brightwave Audiology Letterhead redesign project

We need a full redesign of our current letterhead to make it consistent with the look and feel of our website design www.brightwaveaudio.com.au. It will need to include all information on the current version attached. The letterhead is used for sending medical reports and general correspondence. It should make use of our corporate colours (purple and teal) as per the logo on the existing file. The letterhead should be bold and eye-catching.

Target Market(s)

Medical practitioners.

Font styles to use
Sans Serif

Requirements
Must have
• It will need to include all information on the current version. Must have a premium, professional, high-end look and feel.
Nice to have
• Bold and eye-catching letterhead that reinforces the Brightwave Audiology brand. To stand out from other traditional letterheads.
Should not have
• The design should not be too cluttered or 'busy'

```html
<!DOCTYPE html>
<html lang="en">
<head>
<meta charset="utf-8">
<title>Brightwave Audiology Letterhead</title>
<link href="https://fonts.googleapis.com/css2?family=Fira+Sans:wght@400;600;700&family=Nunito:wght@900&display=swap" rel="stylesheet">
<style>
  :root {
    --backdrop: #d1d2d4;
    --paper: #ffffff;
    --purple: #6f2c91;
    --purple-band: #7b3596;
    --teal: #12b592;
    --ink: #2a2a2a;
    --body-ink: #555555;
  }
  * { margin: 0; padding: 0; box-sizing: border-box; }
  html, body { width: 1200px; height: 1200px; overflow: hidden; }
  body {
    background: var(--backdrop);
    font-family: "Fira Sans", Arial, sans-serif;
    position: relative;
  }
  .letterhead {
    position: absolute;
    left: 318px; top: 132px;
    width: 579px; height: 818px;
    background: var(--paper);
    box-shadow: 0 6px 10px rgba(0,0,0,0.12);
    overflow: hidden;
  }
  .corner-accent { position: absolute; right: 0; top: 0; width: 128px; height: 122px; }
  .brand {
    position: absolute; left: 0; right: 0; top: 66px;
    text-align: center;
  }
  .brand-name {
    font-family: "Nunito", sans-serif; font-weight: 900;
    font-size: 25px; color: var(--purple); letter-spacing: -0.3px;
  }
  .brand-address { margin-top: 14px; font-size: 10px; color: var(--ink); }
  .recipient { position: absolute; left: 72px; top: 183px; color: var(--ink); }
  .recipient .salutation { font-size: 10px; font-weight: 700; }
  .recipient .blank { display: inline-block; width: 55px; border-bottom: 1px solid var(--ink); }
  .recipient .role { font-size: 6px; margin-top: 1px; }
  .recipient .company { font-size: 6.5px; font-weight: 700; margin-top: 3px; letter-spacing: 0.2px; }
  .letter-date {
    position: absolute; right: 60px; top: 183px;
    font-size: 10px; font-weight: 700; color: var(--ink); letter-spacing: 0.3px;
  }
  .letter-body {
    position: absolute; left: 72px; top: 252px; width: 448px;
    font-size: 9.1px; line-height: 11.65px; color: var(--body-ink);
    text-align: justify;
  }
  .letter-body p { margin-bottom: 13px; }
  .letter-body p.lead { font-weight: 700; color: var(--ink); font-size: 9.6px; letter-spacing: 0.15px; margin-bottom: 12px; }
  .sign-off { position: absolute; left: 72px; top: 614px; }
  .signature-area {
    width: 86px; height: 22px; border-bottom: 1px solid var(--ink);
    background: linear-gradient(90deg, rgba(60,60,60,0.08), rgba(60,60,60,0.02));
  }
  .sender-name { margin-top: 12px; font-size: 12px; font-weight: 700; color: var(--purple); letter-spacing: 0.6px; margin-left: 1px; }
  .sender-role { font-size: 8.5px; color: var(--ink); margin-left: 1px; margin-top: 1px; }
  .contact-row { position: absolute; left: 0; top: 738px; width: 100%; }
  .contact-item {
    position: absolute; width: 120px; margin-left: -60px;
    text-align: center; font-size: 6.5px; color: var(--ink);
  }
  .contact-item svg { display: block; margin: 0 auto 10px; }
  .footer-band { position: absolute; left: 0; bottom: 0; width: 100%; height: 10px; background: var(--purple-band); }
</style>
</head>
<body>
  <main class="letterhead">
    <svg class="corner-accent" viewBox="0 0 128 122" aria-hidden="true">
      <path d="M0 0 H128 V82 C90 90 50 76 28 52 C8 32 0 14 0 0 Z" fill="var(--teal)"/>
    </svg>

    <header class="brand">
      <div class="brand-name">Brightwave Audiology</div>
      <div class="brand-address">48 Calder Street, Ridgefield, Qld 4352</div>
    </header>

    <section class="recipient">
      <div class="salutation">Dear, Mr<span class="blank"></span></div>
      <div class="role">Designation</div>
      <div class="company">COMPANY NAME</div>
    </section>
    <div class="letter-date">DATE:16/02/2018</div>

    <article class="letter-body">
      <p>Lorem Ipsum is simply dummy text of the printing and typesetting industry. Lorem Ipsum has been the industry's standard dummy text ever since the1500s,when an unknown printer took a galley of type and scrambled it to make a type specimen book. It has survived not only five centuries, but also the leap into electronic typesetting, remaining essentially unchanged. It was popularised in the 1960s with the release of Letraset sheets containing Lorem Ipsum passages,and more recently with desktop publishing software like Aldus PageMaker including versions of Lorem Ipsum.</p>
      <p>Lorem Ipsum is simply dummy text of the printing and typesetting industry. Lorem Ipsum has been the industry's standard dummy text ever since the1500s,when an unknown printer took a galley of type and scrambled it to make a type specimen book. It has survived not only five centuries, but also the leap into electronic typesetting, remaining essentially unchanged. It was popularised in the 1960s with the release of Letraset sheets containing Lorem Ipsum passages,and more recently with desktop publishing software like Aldus PageMaker including versions of Lorem Ipsum.</p>
      <p class="lead">Lorem Ipsum is simply dummy text of the printing and typesetting industry. Lorem Ipsum has been the industry's standard dummy text ever since the1500s,when an unknown printer took a galley of type and scrambled it to make a type specimen book.</p>
      <p>Lorem Ipsum is simply dummy text of the printing and typesetting industry. Lorem Ipsum has been the industry's standard dummy text ever since the1500s,when an unknown printer took a galley of type and scrambled it to make a type specimen book. It has survived not only five centuries, but also the leap into electronic typesetting, remaining essentially unchanged. It was popularised in the 1960s with the release of Letraset sheets containing Lorem Ipsum passages,and more recently with desktop publishing software like Aldus PageMaker including versions of Lorem Ipsum.</p>
      <p>Lorem Ipsum is simply dummy text of the printing and typesetting industry. Lorem Ipsum has been the industry's standard dummy text ever since the1500s,when an unknown printer took a galley of type and scrambled it to make a type specimen book.</p>
    </article>

    <section class="sign-off">
      <div class="signature-area" role="img" aria-label="Handwritten signature"></div>
      <div class="sender-name">YOUR NAME</div>
      <div class="sender-role">Designation</div>
    </section>

    <footer class="contact-row">
      <div class="contact-item" style="left:125px">
        <svg width="15" height="15" viewBox="0 0 16 16" aria-hidden="true">
          <circle cx="8" cy="8" r="8" fill="var(--purple)"/>
          <path d="M5.4 4.3l1.3 1.5-.7 1c.5 1 1.3 1.8 2.3 2.3l1-.7 1.5 1.3-.9 1.1C7.8 10.6 5.4 8.2 4.3 5.2z" fill="none" stroke="#fff" stroke-width="0.9" stroke-linejoin="round"/>
        </svg>
        +07 4510 2260
      </div>
      <div class="contact-item" style="left:230px">
        <svg width="15" height="15" viewBox="0 0 16 16" aria-hidden="true">
          <circle cx="8" cy="8" r="8" fill="var(--purple)"/>
          <rect x="4.5" y="6" width="7" height="4.5" rx="0.6" fill="none" stroke="#fff" stroke-width="0.9"/>
          <rect x="5.8" y="4.4" width="4.4" height="1.8" fill="none" stroke="#fff" stroke-width="0.8"/>
        </svg>
        +07 4510 2261
      </div>
      <div class="contact-item" style="left:336px">
        <svg width="15" height="15" viewBox="0 0 16 16" aria-hidden="true">
          <circle cx="8" cy="8" r="8" fill="var(--purple)"/>
          <rect x="4.5" y="5.3" width="7" height="5.2" fill="none" stroke="#fff" stroke-width="0.9"/>
          <path d="M4.6 5.5L8 8.2l3.4-2.7" fill="none" stroke="#fff" stroke-width="0.9"/>
        </svg>
        hello@brightwaveaudio.com.au
      </div>
      <div class="contact-item" style="left:442px">
        <svg width="15" height="15" viewBox="0 0 16 16" aria-hidden="true">
          <circle cx="8" cy="8" r="8" fill="var(--purple)"/>
          <circle cx="8" cy="8" r="3.6" fill="none" stroke="#fff" stroke-width="0.9"/>
          <path d="M4.4 8h7.2M8 4.4c-1.4 1.8-1.4 5.4 0 7.2M8 4.4c1.4 1.8 1.4 5.4 0 7.2" fill="none" stroke="#fff" stroke-width="0.7"/>
        </svg>
        hello@brightwaveaudio.com.au
      </div>
    </footer>

    <div class="footer-band"></div>
  </main>
</body>
</html>
```